Ridgemont Business Card Redesign

Using the current logo/tagline lock-up and icon, redesign the Ridgemont business card to better show the tagline and improve the layout to give the card a more timely design and a classic, sophisticated look. See attached Project Brief for more detail.

```html
<!DOCTYPE html>
<html lang="en">
<head>
<meta charset="utf-8">
<title>Ridgemont Capital – Business Card</title>
<link rel="stylesheet" href="https://fonts.googleapis.com/css2?family=EB+Garamond:ital,wght@0,400;0,500;1,400&display=swap">
<style>
  :root {
    --bg: #e9e9e7;
    --card: #ffffff;
    --brand-blue: #1f6bb5;
    --ink: #3a3a3a;
    --rule: #9a9a9a;
  }
  * { margin: 0; padding: 0; box-sizing: border-box; }
  html, body { width: 1200px; height: 800px; overflow: hidden; background: var(--bg); }
  body { display: flex; align-items: center; justify-content: center; font-family: "EB Garamond", Georgia, serif; }

  .card {
    position: relative;
    width: 900px; height: 514px;
    background: var(--card);
    box-shadow: 0 10px 30px rgba(0,0,0,.12);
    display: flex;
  }

  .brand-side {
    width: 470px;
    padding: 56px 40px 52px 56px;
    display: flex; flex-direction: column; justify-content: space-between;
  }
  .lockup { display: flex; flex-direction: column; gap: 12px; }
  .lockup-name { display: flex; align-items: center; gap: 16px; }
  .lockup-mark { width: 54px; height: 54px; border-radius: 50%; background: var(--brand-blue); flex: none; }
  .company-name {
    color: var(--brand-blue); font-size: 38px; font-weight: 500;
    letter-spacing: .05em; text-transform: uppercase; line-height: 1.02;
  }
  .tagline {
    color: var(--ink); font-size: 17px; font-style: italic;
    padding-left: 70px;
  }
  .website { color: var(--brand-blue); font-size: 19px; }

  .divider { width: 1px; background: var(--rule); margin: 44px 0; }

  .contact-side { flex: 1; padding: 60px 40px 50px 50px; color: var(--ink); }
  .person-name { color: var(--brand-blue); font-size: 36px; font-weight: 400; line-height: 1.05; }
  .person-title { font-style: italic; font-size: 21px; line-height: 1.2; margin-top: 6px; padding-left: 30px; }
  .title-rule { width: 230px; height: 1px; background: var(--rule); margin: 18px 0 16px 30px; }
  .phones { display: grid; grid-template-columns: auto auto; column-gap: 12px; justify-content: start; font-size: 20px; line-height: 1.3; }
  .email { font-size: 20px; margin-top: 14px; }
  .address { font-size: 20px; line-height: 1.3; margin-top: 12px; font-style: normal; }
</style>
</head>
<body>
  <article class="card">
    <section class="brand-side">
      <div class="lockup">
        <div class="lockup-name">
          <span class="lockup-mark" aria-hidden="true"></span>
          <span class="company-name">Ridgemont Capital</span>
        </div>
        <span class="tagline">Patient Minority Equity Partners</span>
      </div>
      <div class="website">www.ridgemontcapital.com</div>
    </section>

    <div class="divider" aria-hidden="true"></div>

    <section class="contact-side">
      <h1 class="person-name">Daniel R. Whitcomb</h1>
      <p class="person-title">Principal &amp;<br>Chief Marketing Officer</p>
      <div class="title-rule" aria-hidden="true"></div>
      <div class="phones">
        <span>Office:</span><span>(978) 555-0142</span>
        <span>Cell:</span><span>(804) 555-0187</span>
      </div>
      <p class="email">dwhitcomb@ridgemontcapital.com</p>
      <address class="address">41 Alder Ridge Road<br>Suite 310<br>Millbrook, CT 06890</address>
    </section>
  </article>
</body>
</html>
```